New business blog needs wordpress theme

I need a unique wordpress theme for my new business oriented blog at quietharlow.net. The blog focuses on my experience as an entrepreneur and offers insights into business problems while chronicling my experience building a new company.

I would like to see a theme that looks more like a creative professional's website, not a business website. Large photos, bright colors, unique layout. I do not want stock photos of people in suits doing business type things. Also, no pictures of me - I am blogging anonymously.

The design should communicate technology and beauty - for example, I really like the feel of the landing page at www.pebblyn.net - it is beautiful to look at but also reflects the cutting edge nature of what they are doing.

Industry/Entity Type

Business

```html
<!DOCTYPE html>
<html lang="en">
<head>
<meta charset="utf-8">
<title>quietharlow — Harlow Talks Business</title>
<link rel="stylesheet" href="https://fonts.googleapis.com/css2?family=Comfortaa:wght@400;700&family=Righteous&family=PT+Sans:wght@400;700&display=swap">
<style>
  :root {
    --teal: #6fbba6;
    --teal-deep: #00917f;
    --teal-title: #1f8a6c;
    --green-button: #5cb37a;
    --ink: #111111;
    --white: #ffffff;
    --nav-text: #333333;
    --placeholder: #999999;
    --footer-bg: rgba(55, 55, 55, 0.78);
  }
  * { margin: 0; padding: 0; box-sizing: border-box; }
  html, body { width: 1200px; height: 780px; overflow: hidden; }
  body { position: relative; font-family: "PT Sans", sans-serif; background: #d9d6c4; }

  .hero-photo {
    position: absolute; inset: 0;
    background:
      radial-gradient(ellipse 60% 30% at 75% 70%, rgba(240,235,230,0.55), transparent 70%),
      linear-gradient(180deg, #e3e4d2 0%, #dcdcc6 30%, #c9b59a 45%, #b57a4c 60%, #a0603a 78%, #8f5634 100%);
  }
  .top-band { position: absolute; top: 0; left: 0; width: 1200px; height: 6px; background: var(--teal); }

  .brand {
    position: absolute; left: 78px; top: 36px;
    font-family: "Comfortaa", sans-serif; font-weight: 700;
    font-size: 46px; color: var(--white); letter-spacing: -1px;
  }

  .main-nav { position: absolute; top: 6px; left: 472px; display: flex; height: 112px; }
  .main-nav a {
    display: flex; align-items: flex-end; justify-content: center;
    padding-bottom: 17px; height: 112px;
    font-size: 14px; font-weight: 700; text-transform: uppercase;
    color: var(--nav-text); text-decoration: none;
  }
  .main-nav a.is-active { background: var(--teal); color: var(--white); }
  .main-nav .caret { width: 10px; height: 7px; margin-left: 8px; margin-bottom: 3px; }

  .headline {
    position: absolute; top: 188px; width: 100%; text-align: center;
    font-family: "Righteous", sans-serif; font-size: 30px; letter-spacing: 1px;
    color: var(--teal-title); text-transform: uppercase;
  }
  .tagline {
    position: absolute; top: 228px; width: 100%; text-align: center;
    font-family: "Comfortaa", sans-serif; font-size: 23px; color: var(--ink);
  }

  .signup {
    position: absolute; left: 315px; top: 342px; width: 558px; height: 79px;
    background: var(--teal-deep); border-radius: 14px; padding: 8px;
  }
  .signup-field {
    width: 100%; height: 100%; background: var(--white); border-radius: 10px;
    display: flex; align-items: center; justify-content: center;
    font-family: Arial, sans-serif; font-size: 19px; color: var(--placeholder);
  }

  .post-button {
    position: absolute; left: 453px; top: 503px; width: 294px; height: 81px;
    border: 2px solid var(--white); background: rgba(255,255,255,0.72);
    display: flex; align-items: center; justify-content: center;
    font-family: "Righteous", sans-serif; font-size: 30px; letter-spacing: 1.5px;
    color: var(--ink); text-transform: uppercase;
  }

  .scroll-down { position: absolute; left: 576px; top: 663px; width: 48px; height: 48px; }

  .site-footer {
    position: absolute; left: 0; bottom: 0; width: 1200px; height: 44px;
    background: var(--footer-bg); display: flex; align-items: center;
  }
  .footer-brand {
    position: absolute; left: 79px; top: 9px;
    font-family: "Comfortaa", sans-serif; font-weight: 700; font-size: 21px;
    color: #e8e8e8;
  }
  .footer-nav { position: absolute; right: 76px; top: 14px; display: flex; gap: 27px; }
  .footer-nav a { color: var(--white); text-decoration: none; font-size: 15px; }
</style>
</head>
<body>
  <div class="hero-photo" role="img" aria-label="Photo of a laptop, glasses and a mouse on a wooden desk"></div>
  <div class="top-band"></div>

  <div class="brand">quietharlow</div>

  <nav class="main-nav">
    <a href="#" class="is-active" style="width:83px">Home</a>
    <a href="#" style="width:71px">Post</a>
    <a href="#" style="width:157px">Small Business
      <svg class="caret" viewBox="0 0 10 7"><path d="M1 1l4 4 4-4" fill="none" stroke="#333" stroke-width="2"/></svg></a>
    <a href="#" style="width:111px">Technology</a>
    <a href="#" style="width:96px">About</a>
    <a href="#" style="width:135px">Contact</a>
  </nav>

  <h1 class="headline">Harlow Talks Business</h1>
  <p class="tagline">Best practices, articles and tips and about small business in the United States.</p>

  <div class="signup"><div class="signup-field">--------Enter Your Email--------</div></div>

  <div class="post-button">Post Your Blog</div>

  <svg class="scroll-down" viewBox="0 0 48 48" aria-label="Scroll down">
    <circle cx="24" cy="24" r="23" fill="var(--green-button)" stroke="#4a9a66" stroke-width="1"/>
    <path d="M17 16l7 7 7-7M17 25l7 7 7-7" fill="none" stroke="#fff" stroke-width="3" stroke-linecap="round" stroke-linejoin="round"/>
  </svg>

  <footer class="site-footer">
    <div class="footer-brand">quietharlow</div>
    <nav class="footer-nav">
      <a href="#">Home</a><a href="#">Post</a><a href="#">Small Business</a>
      <a href="#">Technology</a><a href="#">About</a><a href="#">Contact</a>
    </nav>
  </footer>
</body>
</html>
```